CalmHarbor Homepage and Landing Pages

Please see detailed brief.

CalmHarbor is Australia’s newest online therapy and mental health service. We allow patients from across australia to connect with Mental health practitioners from across Australia. Our mission is to remove the friction in gaining support for mental health related issues.

Number of Pages Required

1 page

Font styles to use
Sans Serif

Colors
33a6d7
0293ce
3277b5
0255a3
acd136
9bcb3c

Requirements
Must have
• Please see detailed brief.
Nice to have
• Please see detailed brief
Should not have

```html
<!DOCTYPE html>
<html lang="en">
<head>
<meta charset="utf-8">
<title>CalmHarbor — Online Therapy &amp; Mental Health</title>
<link href="https://fonts.googleapis.com/css2?family=Bebas+Neue&family=Roboto+Condensed:wght@300;400;700&family=Montserrat:wght@400;500;600;700;800&family=Kaushan+Script&display=swap" rel="stylesheet">
<style>
  :root{
    --blue:#0a57d8;
    --blue-band:#0752d6;
    --blue-bright:#2f86f0;
    --blue-light:#8fb6f2;
    --ink:#1b1b1b;
    --text:#2a2a2a;
    --white:#ffffff;
    --orange:#f26522;
    --field:#ececec;
    --slate:#4b5a7c;
    --beige-1:#e2cdbb;
    --beige-2:#c9a890;
  }
  *{box-sizing:border-box;margin:0;padding:0}
  html,body{width:1200px;height:4085px;overflow:hidden;background:var(--white)}
  body{position:relative;font-family:"Roboto Condensed",Arial,sans-serif;color:var(--text)}

  /* header */
  .site-header{position:absolute;left:0;top:0;width:1200px;height:111px;background:var(--white);z-index:5}
  .brand{position:absolute;left:30px;top:34px;display:flex;align-items:center;gap:12px;font-family:"Montserrat",sans-serif;font-weight:400;font-size:38px;color:var(--ink);line-height:1;white-space:nowrap}
  .brand-dot{width:30px;height:30px;border-radius:50%;background:var(--blue);flex-shrink:0}
  .main-nav{position:absolute;left:352px;top:49px;font-family:"Montserrat",sans-serif;font-size:13px;font-weight:500;color:#3a3a3a;letter-spacing:.3px;white-space:nowrap}
  .main-nav span{margin:0 6px;color:#777}
  .login{position:absolute;left:906px;top:47px;display:flex;align-items:center;gap:8px;font-family:"Montserrat",sans-serif;font-size:12px;font-weight:700;color:#333;white-space:nowrap}
  .signin{position:absolute;left:1008px;top:44px;width:156px;height:33px;border-radius:17px;background:var(--blue);color:var(--white);font-family:"Montserrat",sans-serif;font-size:11px;font-weight:700;display:flex;align-items:center;padding-left:16px;gap:10px;white-space:nowrap}
  .signin .mini-arrow{width:22px;height:22px;border-radius:50%;background:var(--blue-bright);display:flex;align-items:center;justify-content:center;flex-shrink:0}

  /* hero */
  .hero{position:absolute;left:0;top:111px;width:1200px;height:760px;overflow:hidden}
  .hero-photo{position:absolute;inset:0;background:radial-gradient(ellipse at 85% 40%,#b9d8a8 0%,rgba(185,216,168,0) 30%),linear-gradient(120deg,var(--beige-1) 0%,#d7bca6 55%,var(--beige-2) 100%)}
  .hero-wave{position:absolute;left:0;top:470px;width:1200px;height:290px}
  .hero-greet{position:absolute;left:96px;top:120px;font-weight:300;font-size:62px;color:var(--ink);line-height:1;white-space:nowrap}
  .hero-title{position:absolute;left:94px;top:182px;font-family:"Bebas Neue",sans-serif;font-weight:400;font-size:118px;color:var(--ink);line-height:1;letter-spacing:1px;white-space:nowrap}
  .hero-copy{position:absolute;left:98px;top:298px;width:440px;font-size:24px;line-height:35px;color:var(--ink)}
  .hero-phone{position:absolute;left:682px;top:67px;width:302px;height:615px;border-radius:46px;background:linear-gradient(180deg,#f2f2f2,#d9d9d9);border:2px solid #c8c8c8}
  .hero-phone .screen{position:absolute;left:16px;top:68px;width:266px;height:478px;background:linear-gradient(180deg,#1a4fe0,#0b3fcf)}
  .hero-dots{position:absolute;left:1142px;top:249px;display:flex;flex-direction:column;gap:10px}
  .hero-dots i{display:block;width:12px;height:12px;border-radius:50%;background:var(--white)}
  .hero-dots i:first-child{background:transparent;border:2px solid var(--white)}

  /* buttons */
  .btn{position:absolute;display:flex;align-items:center;justify-content:space-between;gap:12px;border-radius:32px;background:var(--blue);color:var(--white);font-family:"Montserrat",sans-serif;font-weight:700;font-size:19px;padding:0 10px 0 24px;white-space:nowrap}
  .btn .ring{width:38px;height:38px;border-radius:50%;display:flex;align-items:center;justify-content:center;flex-shrink:0}
  .ring--bright{background:var(--blue-bright)}
  .ring--white{background:var(--white)}

  /* shared headings */
  .eyebrow{font-size:23px;color:var(--ink);letter-spacing:.5px}
  .display{font-family:"Bebas Neue",sans-serif;font-weight:400;line-height:1;letter-spacing:1px;white-space:nowrap}
  .rule{position:absolute;height:2px;width:106px}
  .body-copy{font-size:20.5px;line-height:31px;text-align:justify}

  /* about */
  .about-art{position:absolute;left:95px;top:903px;width:478px;height:400px;border-radius:48% 52% 46% 54%/50% 44% 56% 50%;background:linear-gradient(160deg,#e3ecfb,#c6d8f6)}
  .about-eyebrow{position:absolute;left:598px;top:893px}
  .about-title{position:absolute;left:597px;top:924px;font-size:66px;color:var(--blue)}
  .about-copy{position:absolute;left:598px;top:1023px;width:503px;color:var(--ink)}

  /* mission */
  .mission{position:absolute;left:0;top:1355px;width:1200px;height:547px;background:linear-gradient(135deg,#0b5ce0 0%,var(--blue-band) 60%,#0448c8 100%)}
  .mission-title{position:absolute;left:133px;top:150px;font-size:64px;color:var(--white)}
  .mission-copy{position:absolute;left:133px;top:253px;width:510px;color:var(--white);text-align:left}
  .mission-devices{position:absolute;left:748px;top:56px;width:354px;height:452px;background:linear-gradient(160deg,#2b2b2b 0%,#3d3d3d 55%,#e9eef7 56%,#ffffff 100%);border-radius:8px}

  /* find */
  .find{position:absolute;left:0;top:1902px;width:1200px;height:618px}
  .find-phone{position:absolute;left:209px;top:92px;width:229px;height:432px;background:#1d1d1d;border-radius:6px}
  .find-phone .screen{position:absolute;left:12px;top:30px;width:205px;height:360px;background:linear-gradient(180deg,#f4f7fc,#e4ebf7)}
  .find-script{position:absolute;left:516px;top:100px;font-family:"Kaushan Script",cursive;font-size:58px;color:var(--ink);line-height:1}
  .find-title{position:absolute;left:521px;top:178px;font-size:66px;color:var(--blue)}
  .find-copy{position:absolute;left:521px;top:272px;width:508px;color:var(--ink)}
  .find-tag{position:absolute;left:521px;top:403px;font-weight:700;font-size:21px;color:var(--ink)}

  /* team */
  .team{position:absolute;left:0;top:2520px;width:1200px;height:714px;background:linear-gradient(135deg,#0b5ce0 0%,var(--blue-band) 60%,#0448c8 100%)}
  .team-title{position:absolute;left:133px;top:68px;font-size:64px;color:var(--white)}
  .team-copy{position:absolute;left:133px;top:168px;width:504px;color:var(--white);font-size:20.5px;line-height:27px;text-align:justify}
  .team-copy p+p{margin-top:27px}
  .team-card{position:absolute;left:706px;top:74px;width:398px;height:566px;border:4px solid var(--white);border-radius:14px;overflow:hidden;background:var(--slate)}
  .team-photo{position:absolute;left:0;top:0;width:100%;height:438px;background:radial-gradient(ellipse at 50% 45%,#6b6b6b 0%,#2a2a2a 55%,#141414 100%)}
  .team-caption{position:absolute;left:0;top:438px;width:100%;text-align:center;color:var(--white)}
  .team-caption h3{font-family:"Bebas Neue",sans-serif;font-weight:400;font-size:34px;margin-top:10px;letter-spacing:1px}
  .team-caption p{font-weight:300;font-size:26px;line-height:32px}

  /* contact */
  .contact-card{position:absolute;left:97px;top:3313px;width:1003px;height:483px;background:var(--white);box-shadow:0 4px 18px rgba(0,0,0,.13)}
  .contact-intro{position:absolute;left:0;top:0;width:410px;height:483px;background:var(--blue);color:var(--white);text-align:center}
  .contact-intro h2{position:absolute;left:0;width:410px;top:162px;font-family:"Montserrat",sans-serif;font-weight:800;font-size:42px;letter-spacing:.5px;white-space:nowrap}
  .contact-intro p.lead{position:absolute;left:40px;width:330px;top:228px;font-size:19px;line-height:24px}
  .contact-note{position:absolute;left:33px;top:320px;width:349px;height:81px;border:1px solid rgba(255,255,255,.7);border-radius:4px;font-family:"Montserrat",sans-serif;font-weight:700;font-size:13.5px;line-height:19px;display:flex;align-items:center;justify-content:center}
  .contact-form{position:absolute;left:445px;top:0;width:530px;height:483px;color:#333}
  .contact-form h2{position:absolute;left:0;top:30px;font-family:"Montserrat",sans-serif;font-weight:700;font-size:25px;color:var(--orange);white-space:nowrap}
  .label{position:absolute;font-size:14px;color:#333}
  .field{position:absolute;background:var(--field)}
  .check{position:absolute;display:flex;align-items:center;gap:12px;font-size:14px;white-space:nowrap}
  .check i{display:block;width:22px;height:22px;border:1.5px solid #555;background:var(--white)}
  .submit{position:absolute;left:-3px;top:415px;width:139px;height:48px;border-radius:24px;background:#222;color:var(--white);font-family:"Montserrat",sans-serif;font-weight:700;font-size:17px;display:flex;align-items:center;justify-content:center}

  /* footer */
  .site-footer{position:absolute;left:0;top:3830px;width:1200px;height:255px;text-align:center}
  .footer-brand{position:absolute;left:0;width:1200px;top:20px;display:flex;justify-content:center;align-items:center;gap:14px;font-family:"Montserrat",sans-serif;font-weight:400;font-size:46px;color:var(--ink);line-height:1}
  .footer-brand .brand-dot{width:36px;height:36px}
  .social{position:absolute;left:0;width:1200px;top:90px;display:flex;justify-content:center;gap:18px}
  .social i{display:block;width:46px;height:46px;border-radius:50%;background:#9bbcf5}
  .footer-links{position:absolute;left:0;width:1200px;top:155px;font-family:"Montserrat",sans-serif;font-weight:700;font-size:15.5px;color:var(--ink)}
  .footer-links span{margin:0 5px;font-weight:400}
  .copyright{position:absolute;left:0;width:1200px;top:188px;font-size:15px;color:#333}
</style>
</head>
<body>

<header class="site-header">
  <div class="brand"><span class="brand-dot"></span>CalmHarbor</div>
  <nav class="main-nav">FOR PRACTITIONERS<span>|</span>HOW IT WORKS<span>|</span>MEET OUR TEAM<span>|</span>CONTACT</nav>
  <div class="login">
    <svg width="22" height="22" viewBox="0 0 22 22"><circle cx="11" cy="11" r="9.5" fill="none" stroke="#0a57d8" stroke-width="1.6"/><circle cx="11" cy="9" r="3" fill="none" stroke="#0a57d8" stroke-width="1.6"/><path d="M5.5 17c1.5-2.5 3.3-3.5 5.5-3.5s4 1 5.5 3.5" fill="none" stroke="#0a57d8" stroke-width="1.6"/></svg>
    LOG IN
  </div>
  <div class="signin">PATIENT SIGN IN
    <span class="mini-arrow"><svg width="10" height="12" viewBox="0 0 10 12"><path d="M3 1l5 5-5 5" fill="none" stroke="#fff" stroke-width="1.8"/></svg></span>
  </div>
</header>

<section class="hero">
  <div class="hero-photo" role="img" aria-label="Close-up photo of hands holding a green awareness ribbon"></div>
  <svg class="hero-wave" viewBox="0 0 1200 290" preserveAspectRatio="none">
    <path d="M0 90 C180 200 420 250 690 230 C900 214 1060 150 1200 250 L1200 290 L0 290 Z" fill="#ffffff"/>
    <path d="M0 104 C190 214 430 262 690 242 C900 226 1070 165 1200 262" fill="none" stroke="#0a57d8" stroke-width="5"/>
    <path d="M930 200 C1040 175 1130 205 1200 250 L1200 290 C1130 240 1040 215 930 220 Z" fill="#0a57d8"/>
  </svg>
  <div class="hero-greet">Welcome to</div>
  <h1 class="hero-title">CALMHARBOR</h1>
  <p class="hero-copy">CalmHarbor provides on-demand access to a range of psychologists &amp; personal wellness professionals from across Australia. Book your online appointment in minutes, 24/7.</p>
  <div class="btn" style="left:98px;top:469px;width:322px;height:60px">FIND A PRACTITIONER<span class="ring ring--bright"><svg width="12" height="18" viewBox="0 0 12 18"><path d="M2 2l7 7-7 7" fill="none" stroke="#fff" stroke-width="2.4"/></svg></span></div>
  <div class="hero-phone" role="img" aria-label="Smartphone showing the app loading screen">
    <div class="screen"></div>
  </div>
  <div class="hero-dots"><i></i><i></i><i></i><i></i></div>
</section>

<section class="about">
  <div class="about-art" role="img" aria-label="Illustration of a person selecting a date on a large calendar beside a clock"></div>
  <div class="about-eyebrow eyebrow">ABOUT US</div>
  <h2 class="about-title display">WHAT IS CALMHARBOR?</h2>
  <div class="rule" style="left:599px;top:1003px;background:#333"></div>
  <p class="about-copy body-copy">CalmHarbor is Australia’s newest online therapy and mental health service. We allow patients from across australia to connect with Mental health practitioners from across Australia. Our mission is to remove the friction in gaining support for mental health related issues.</p>
  <div class="btn" style="left:631px;top:1209px;width:191px;height:59px;border-radius:0 30px 30px 0;padding-left:0">READ MORE<span class="ring ring--bright"><svg width="12" height="18" viewBox="0 0 12 18"><path d="M2 2l7 7-7 7" fill="none" stroke="#fff" stroke-width="2.4"/></svg></span></div>
</section>

<section class="mission">
  <h2 class="mission-title display">OUR MISSION IS SIMPLE</h2>
  <div class="rule" style="left:133px;top:230px;background:rgba(255,255,255,.8)"></div>
  <p class="mission-copy body-copy">We want to break down the barriers in receiving effective treatment and care for anxiety, stress and mental health related issues.</p>
  <div class="btn" style="left:133px;top:385px;width:229px;height:57px;background:var(--blue-bright)">HOW IT WORK<span class="ring ring--white"><svg width="12" height="18" viewBox="0 0 12 18"><path d="M2 2l7 7-7 7" fill="none" stroke="#222" stroke-width="2.2"/></svg></span></div>
  <div class="mission-devices" role="img" aria-label="Tablet showing a video call with a practitioner and a phone showing a booking calendar"></div>
</section>

<section class="find">
  <div class="find-phone" role="img" aria-label="Phone showing a practitioner profile with a Book Now button">
    <div class="screen"></div>
  </div>
  <div class="find-script">Find</div>
  <h2 class="find-title display">THE HELP YOU NEED</h2>
  <div class="rule" style="left:521px;top:254px;background:#333"></div>
  <p class="find-copy body-copy">Book an appointment with one of our highly qualified, licensed practitioners.The consultation can be conducted from wherever you feel most comfortable.</p>
  <p class="find-tag">No travel. No Clinics.</p>
  <div class="btn" style="left:515px;top:455px;width:321px;height:59px">FIND A PRACTITIONER<span class="ring ring--bright"><svg width="12" height="18" viewBox="0 0 12 18"><path d="M2 2l7 7-7 7" fill="none" stroke="#fff" stroke-width="2.4"/></svg></span></div>
</section>

<section class="team">
  <h2 class="team-title display">MEET OUR TEAM</h2>
  <div class="team-copy">
    <p>Dr Martin Kell is an Australian neuroscientist in private practice specializing in brain performance. He has a bachelor’s degree in psychology and a doctorate of science in biological statistics. Dr Kell has worked as a psychologist for over 30 years and more recently has focused on the neurosciences.</p>
    <p>Martin has helped many people, schools, sporting teams and organisations with improving performance and in particular memory, concentration, agility and resilience. It was through the discovery of the positive neurological effects of colouring-in using Dr Kell’s designs which has sparked a worldwide sensation resulting in three of Dr Kell’s colouring-in brain science books being featured by Helena Gray in her 2016 Christmas Wish List.</p>
  </div>
  <div class="btn" style="left:133px;top:607px;width:229px;height:57px;background:var(--blue-bright)">READ MORE<span class="ring ring--white"><svg width="12" height="18" viewBox="0 0 12 18"><path d="M2 2l7 7-7 7" fill="none" stroke="#222" stroke-width="2.2"/></svg></span></div>
  <div class="team-card">
    <div class="team-photo" role="img" aria-label="Portrait photo of the chief science advisor"></div>
    <div class="team-caption">
      <h3>DR. MARTIN KELL</h3>
      <p>NEUROSCIENTIST &amp; CHIEF<br>SCIENCE ADVISOR</p>
    </div>
  </div>
</section>

<section class="contact-card">
  <div class="contact-intro">
    <h2>GET IN TOUCH!</h2>
    <p class="lead">Whether you are a Patient, Practitioner or just want to learn more. Feel free to drop us a line.</p>
    <div class="contact-note">Please submit your details below and<br>we’ll be in touch at the earliest opportunity,<br>or contact us by phone on 100200300.</div>
  </div>
  <form class="contact-form">
    <h2>CONTACT CALMHARBOR TODAY</h2>
    <span class="label" style="left:0;top:75px">Name</span>
    <span class="field" style="left:0;top:98px;width:520px;height:30px"></span>
    <span class="label" style="left:0;top:144px">I am a:</span>
    <span class="check" style="left:0;top:170px"><i></i>PATIENT</span>
    <span class="check" style="left:257px;top:170px"><i></i>MENTAL HEALTH PRACTITIONER</span>
    <span class="label" style="left:0;top:210px">Email</span>
    <span class="field" style="left:0;top:234px;width:240px;height:31px"></span>
    <span class="label" style="left:284px;top:210px">Phone</span>
    <span class="field" style="left:284px;top:234px;width:236px;height:31px"></span>
    <span class="label" style="left:0;top:278px">Inquiry</span>
    <span class="field" style="left:0;top:304px;width:520px;height:89px"></span>
    <span class="submit">SUBMIT</span>
  </form>
</section>

<footer class="site-footer">
  <div class="footer-brand"><span class="brand-dot"></span>CalmHarbor</div>
  <div class="social"><i></i><i></i></div>
  <div class="footer-links">HELP &amp; FAQ<span>|</span>PRIVACY POLICY<span>|</span>TERMS &amp; CONDITIONS<span>|</span>CONTACT</div>
  <div class="copyright">CalmHarbor &nbsp;| All Rights Reserved &nbsp;© 2020</div>
</footer>

</body>
</html>
```